Vorla Pty Ltd business card design

We need a business card for our company who is involved in upper market residential property development.
Design should be elegant and contemporary.

Our residences are inspired and elegant in contemporary design, combined with inviting ambience. We produce exclusive boutique developments which appeal to the most discerning of purchasers.
We would like to see a design to reflect the above.

Industry/Entity Type

Residential

Contact Information for Business Card

Vorla Pty Ltd, Marek Dunsworth, PO Box 58 Kelvale 3194 Melbourne AUSTRALIA, ph (+61 3) 0427 5926 84

Logo Text

Vorla Pty Ltd

```html
<!DOCTYPE html>
<html lang="en">
<head>
<meta charset="utf-8">
<title>Vorla Pty Ltd business card</title>
<link rel="stylesheet" href="https://fonts.googleapis.com/css2?family=Open+Sans:wght@600;700&display=swap">
<style>
  :root {
    --stage: #262626;
    --stage-edge: #151515;
    --brand-blue: #1a76c4;
    --deep-blue: #1f3c78;
    --panel: #0b111b;
    --ink-black: #080808;
    --paper-white: #f4f6f8;
  }
  * { box-sizing: border-box; margin: 0; padding: 0; }
  html, body {
    width: 1200px; height: 1200px; overflow: hidden;
    background: radial-gradient(circle at 50% 45%, var(--stage), var(--stage-edge));
    font-family: "Open Sans", Arial, sans-serif;
  }
  .card {
    position: absolute; left: 150px;
    width: 900px; height: 500px;
    border-radius: 22px; overflow: hidden;
    box-shadow: 0 18px 40px rgba(0,0,0,.55);
  }
  .card svg { position: absolute; inset: 0; display: block; }
  .card--contact { top: 70px; }
  .card--brand { top: 630px; }

  .contact-block {
    position: absolute; left: 300px; top: 110px; width: 520px;
    color: var(--paper-white); font-weight: 600;
  }
  .contact-name { color: var(--brand-blue); font-size: 34px; line-height: 1.2; margin-bottom: 14px; }
  .contact-line { font-size: 25px; line-height: 1.3; }
  .contact-phone { margin-top: 12px; }
  .contact-phone .label { color: var(--brand-blue); margin-right: 6px; }
  .contact-rule { height: 2px; background: var(--paper-white); margin: 14px 0 16px; }
  .company-row { display: flex; align-items: center; justify-content: flex-end; gap: 18px; }
  .company-mark { width: 34px; height: 34px; background: var(--paper-white); }
  .company-name { font-size: 52px; font-weight: 700; letter-spacing: 2px; color: var(--paper-white); }

  .brand-lockup {
    position: absolute; left: 0; right: 0; top: 205px;
    display: flex; align-items: center; justify-content: center; gap: 22px;
  }
  .brand-mark { width: 44px; height: 44px; background: var(--brand-blue); }
  .brand-name { font-size: 62px; font-weight: 700; letter-spacing: 3px; color: var(--brand-blue); }
</style>
</head>
<body>

<section class="card card--contact" aria-label="Business card, contact side">
  <svg viewBox="0 0 900 500" width="900" height="500" aria-hidden="true">
    <rect class="card-frame" width="900" height="500" fill="var(--brand-blue)"/>
    <path class="card-corner-sweep" d="M0,300 C120,330 200,420 230,500 L0,500 Z" fill="var(--deep-blue)"/>
    <path class="card-right-band" d="M870,0 L900,0 L900,500 L870,500 Z" fill="var(--ink-black)"/>
    <rect class="card-panel" x="40" y="28" width="830" height="444" fill="var(--panel)"/>
  </svg>
  <div class="contact-block">
    <p class="contact-name">Marek Dunsworth</p>
    <p class="contact-line">PO Box 58 Kelvale 3194</p>
    <p class="contact-line">Melbourne AUSTRALIA,</p>
    <p class="contact-line contact-phone"><span class="label">ph</span>(+61 3) 0427 5926 84</p>
    <div class="contact-rule"></div>
    <div class="company-row">
      <span class="company-mark"></span>
      <span class="company-name">Vorla Pty Ltd</span>
    </div>
  </div>
</section>

<section class="card card--brand" aria-label="Business card, brand side">
  <svg viewBox="0 0 900 500" width="900" height="500" aria-hidden="true">
    <rect class="card-top-band" width="900" height="500" fill="var(--brand-blue)"/>
    <path class="card-bottom-sweep" d="M0,300 C250,330 520,420 900,390 L900,500 L0,500 Z" fill="var(--deep-blue)"/>
    <path class="card-wave" d="M0,205 C300,150 620,95 900,130 L900,390 C560,420 260,330 0,315 Z" fill="var(--ink-black)"/>
  </svg>
  <div class="brand-lockup">
    <span class="brand-mark"></span>
    <span class="brand-name">Vorla Pty Ltd</span>
  </div>
</section>

</body>
</html>
```